Flyer for Leaflet Dropping - A5 - Managed IT Support Flyer

I need an A5 double sided flyer LANDSCAPE - design for door to door leaflet dropping / marketing to local businesses.
Our main aim is to promote our ‘Managed IT Support’ services to local small and medium businesses.
Our secondary aim is to promote our additional services which are internet/communications and cloud services. We want to mention these services but they are only secondary therefore need to take a smaller focus and not detract from the main message of the flyer.
• Hosted Cloud Desktop
• VOIP Telephone Systems
• Office 365
• Cloud Services
• Internet Services
• Disaster Recovery

Target Market(s)

Our target audience is senior members of company (MD, FD, Owners, Operations, Management), looking to outsource their IT requirements/needs. UK Only. N London

Industry/Entity Type

Information Technology

Font styles to use
Sans Serif

Requirements
Must have
• Please use the website for a source of information and inspiration – www.brimtek.co.uk.
• We specifically feel the points below are important and want to see them feature.
• 1. Large bold heading highlighting our primary service ‘Managed IT Support’
• 2. Secondary sub-heading explaining exactly what we do.
• ‘We manage your IT ensuring systems are monitored, supported and protected to enhance business growth.’
• 3. Reasons to choose BrimTek – take inspiration from https://www.brimtek.co.uk/about-us/
• 4. No Risk - Our 90 Day Satisfaction Guarantee (see website).
• 5. Areas we cover: ‘Trusted by 100+ businesses across Hertfordshire, Essex, London & beyond.‘
• 6. Name of company, contact details.
• CALL TO ACTION
• 1. Call Us – 03339017462
• 2. Visit our Website – https://www.brimtek.co.uk/gomanaged

```html
<!DOCTYPE html>
<html lang="en">
<head>
<meta charset="utf-8">
<title>BrimTek – Managed IT Support Flyer</title>
<link rel="stylesheet" href="https://fonts.googleapis.com/css2?family=Alfa+Slab+One&family=Arvo:wght@700&family=Gentium+Book+Plus&family=Gabriela&display=swap">
<style>
  :root {
    --sky: #7cc3f2;
    --sky-deep: #4aa6e6;
    --stripe: rgba(255,255,255,0.35);
    --headline-dark: #1c1c1c;
    --headline-mid: #8a8a8a;
    --red: #e0141b;
    --blue-text: #1a1ad6;
    --tag-blue: #1e88d8;
    --pink-band: rgba(232,150,170,0.55);
    --grey-band: rgba(215,215,215,0.8);
    --magenta: #e01ad8;
    --peach: #fbe3b2;
    --orange-band: rgba(245,170,110,0.75);
    --orange-text: #ea6d1e;
    --navy: #1a2740;
    --brand-grey: #6d6d6d;
  }
  * { margin: 0; padding: 0; box-sizing: border-box; }
  html, body { width: 1200px; height: 845px; overflow: hidden; }
  .flyer {
    position: relative;
    width: 1200px; height: 845px;
    background:
      repeating-linear-gradient(125deg, transparent 0 90px, var(--stripe) 90px 170px),
      linear-gradient(180deg, #a9dbfb 0%, var(--sky) 60%, var(--sky-deep) 100%);
    font-family: "Gentium Book Plus", serif;
    overflow: hidden;
  }
  .headline {
    position: absolute; top: 4px; left: 0; width: 1200px;
    text-align: center;
    font-family: "Alfa Slab One", serif;
    font-size: 92px; letter-spacing: 2px;
    background: linear-gradient(180deg, var(--headline-dark) 20%, var(--headline-mid) 55%, var(--headline-dark) 90%);
    -webkit-background-clip: text; background-clip: text;
    color: transparent;
    -webkit-text-stroke: 2px rgba(255,255,255,0.8);
    filter: drop-shadow(0 0 6px rgba(255,255,255,0.9));
  }
  .brand-panel {
    position: absolute; left: 0; top: 140px; width: 168px; height: 695px;
    border-radius: 0 10px 10px 0;
    background: linear-gradient(180deg, #ffffff 0%, #f2f2f2 45%, #9a9a9a 75%, #111 100%);
  }
  .brand-name {
    position: absolute; left: 84px; top: 245px;
    transform: translate(-50%, -50%) rotate(-90deg);
    font-family: "Gentium Book Plus", serif;
    font-size: 104px; color: var(--brand-grey);
    white-space: nowrap;
  }
  .brand-dot {
    position: absolute; left: 44px; bottom: 40px;
    width: 80px; height: 80px; border-radius: 50%;
    background: var(--brand-grey);
  }
  .subheading {
    position: absolute; left: 184px; top: 128px; width: 1010px;
    font-size: 44px; line-height: 60px; color: var(--red);
    white-space: nowrap;
  }
  .tag {
    position: absolute; font-family: "Gabriela", serif; font-weight: 400;
    padding: 0 6px; line-height: 38px; white-space: nowrap;
  }
  .tag--why { left: 530px; top: 258px; background: var(--tag-blue); color: #fff; font-size: 28px; }
  .tag--guarantee { left: 346px; top: 464px; background: var(--tag-blue); color: #fff; font-size: 27px; padding: 0 10px; }
  .tag--areas { left: 506px; top: 709px; background: var(--peach); color: #4a3a10; font-size: 25px; padding: 0 8px; }
  .band { position: absolute; font-family: "Gabriela", serif; }
  .band--why {
    left: 180px; top: 303px; width: 1012px; height: 150px;
    background: var(--pink-band); color: var(--blue-text);
    font-size: 19.5px; line-height: 37px; padding: 0 4px;
    letter-spacing: -0.2px;
  }
  .band--guarantee {
    left: 186px; top: 506px; width: 1003px; height: 210px;
    background: var(--grey-band); color: var(--magenta);
    font-size: 18px; line-height: 34.5px; padding: 2px 6px;
  }
  .band--areas {
    left: 264px; top: 754px; width: 662px; height: 28px;
    background: var(--orange-band); color: var(--orange-text);
    font-size: 18.5px; line-height: 28px; padding: 0 6px;
    white-space: nowrap; overflow: hidden;
  }
  .contact-bar {
    position: absolute; left: 168px; top: 796px; width: 1032px; height: 40px;
    font-family: "Arvo", serif; font-weight: 700; font-size: 21px; color: var(--navy);
  }
  .contact-bar .call { position: absolute; left: 26px; top: 4px; }
  .contact-bar .web { position: absolute; left: 400px; top: 4px; }
</style>
</head>
<body>
<main class="flyer">
  <h1 class="headline">Managed IT Support</h1>

  <aside class="brand-panel">
    <span class="brand-name">BrimTek</span>
    <span class="brand-dot" aria-hidden="true"></span>
  </aside>

  <p class="subheading">We manage your IT ensuring systems are monitored,<br>supported and protected to enhance business growth</p>

  <h2 class="tag tag--why">Why us?</h2>
  <section class="band band--why">
    <p>We are an award winning IT support and strategic services company with over 10 years’ experience of delivering exceptional services to businesses across all sectors.</p>
    <p>Every day over 2,000 people in 100+ companies depend on our support and good expertise and we have grown to be a trusted and reliable provider throughout the UK.</p>
  </section>

  <h2 class="tag tag--guarantee">Our 90 Day Satisfaction Guarantee</h2>
  <section class="band band--guarantee">
    <p>We’re so certain of our service offering that if you are not satisfied, we’ll give you your money back.</p>
    <p>We are commited to providing you the best IT support in the industry. In fact, we are so certain of results, we guarantee your satisfaction. If you do not see satisfactory results in 90 days, we will refund your money.</p>
    <p>How many IT support companies are willing to provide a guarantee for 90 days?</p>
    <p>To eliminate the stress and uncertainity of hiring a competent IT Support company, we’ve decide to offer our clients this ZERO RISK guarantee on all of our Managed Services</p>
  </section>

  <h2 class="tag tag--areas">Areas we cover</h2>
  <p class="band band--areas">Trusted by 100+ businesses across Hertfordshire, Essex, London &amp; beyond</p>

  <footer class="contact-bar">
    <span class="call">Call us: 03339017462</span>
    <span class="web">Visit our Website: www.brimtek.co.uk/gomanaged</span>
  </footer>
</main>
</body>
</html>
```